Quorvex - Automated robotic Inspection with AI need new business cards

We need a new design of our business cards. The company is focused on automated quality control at high speed with unmatched results. We have a logo but need a more forward leaning business card that shows that we are delivering cutting edge technology.

Contact Information for Business Card

Name
Position
Adress
Phone
Email
e.g.
Lena Holmqvist
Chief Financial Officer (CFO)

Quorvex Sweden AB
Bruksvägen 14, SE-175 43 JÄRFÄLLA, Sweden
Mobile: +46735 21 47 83 | Office: +46 8 61 94 27
www.quorvex-example.com

Font styles to use
Sans Serif

```html
<!DOCTYPE html>
<html lang="en">
<head>
<meta charset="utf-8">
<title>Quorvex Business Cards</title>
<link href="https://fonts.googleapis.com/css2?family=Lato:wght@400;700;900&display=swap" rel="stylesheet">
<style>
  :root {
    --brand-blue: #1f5a88;
    --brand-blue-light: #2a6a9c;
    --brand-blue-deep: #184b74;
    --paper: #f7f8f9;
    --ink: #3d4247;
    --stage: #e6e8eb;
  }
  * { margin: 0; padding: 0; box-sizing: border-box; }
  html, body { width: 1200px; height: 896px; overflow: hidden; }
  body {
    background: var(--stage);
    font-family: "Lato", sans-serif;
    display: flex;
    align-items: center;
    justify-content: center;
    gap: 40px;
  }
  .card {
    position: relative;
    width: 540px;
    height: 340px;
    overflow: hidden;
    box-shadow: 0 10px 28px rgba(0,0,0,0.18);
  }
  /* Front */
  .card-front {
    background: linear-gradient(135deg, var(--brand-blue-deep), var(--brand-blue) 55%, var(--brand-blue-light));
    display: flex;
    align-items: center;
    justify-content: center;
    gap: 16px;
  }
  .front-mark {
    width: 44px; height: 44px;
    border-radius: 50%;
    background: var(--brand-blue-light);
  }
  .front-name {
    font-weight: 900;
    font-size: 58px;
    letter-spacing: 2px;
    color: var(--brand-blue-light);
  }
  /* Back */
  .card-back { background: var(--paper); }
  .back-swoosh { position: absolute; inset: 0; width: 100%; height: 100%; }
  .company-lockup {
    position: absolute; left: 34px; top: 40px;
    display: flex; align-items: center; gap: 10px;
  }
  .lockup-mark { width: 22px; height: 22px; border-radius: 50%; background: var(--brand-blue); }
  .lockup-name {
    font-weight: 900; font-size: 34px; letter-spacing: 1px; color: var(--brand-blue);
  }
  .address {
    position: absolute; left: 34px; top: 118px;
    font-size: 13.5px; line-height: 1.35; color: var(--ink);
  }
  .address .legal-name { color: var(--brand-blue); }
  .contacts {
    position: absolute; left: 34px; top: 196px;
    list-style: none; font-size: 13.5px; line-height: 1.5; color: var(--ink);
  }
  .contacts li { display: flex; align-items: center; gap: 8px; }
  .contacts svg { width: 11px; height: 11px; fill: var(--brand-blue); flex: none; }
  .person {
    position: absolute; right: 54px; top: 70px; text-align: left;
  }
  .person-name {
    font-weight: 900; font-size: 21px; color: var(--brand-blue); letter-spacing: 0.3px;
  }
  .person-title { font-size: 13px; color: var(--ink); margin-top: 2px; }
  .website {
    position: absolute; right: 22px; bottom: 20px;
    font-size: 12px; color: #fff; letter-spacing: 0.3px;
  }
  .website b { font-weight: 700; }
</style>
</head>
<body>
  <section class="card card-front" aria-label="Business card front">
    <span class="front-mark"></span>
    <span class="front-name">QUORVEX</span>
  </section>

  <section class="card card-back" aria-label="Business card back">
    <svg class="back-swoosh" viewBox="0 0 540 340" preserveAspectRatio="none" aria-hidden="true">
      <path d="M230 340 C370 300 480 210 518 60 L540 60 L540 340 Z" fill="var(--brand-blue)"/>
      <path d="M210 340 C360 296 470 205 510 48" fill="none" stroke="var(--brand-blue)" stroke-width="4"/>
    </svg>

    <div class="company-lockup">
      <span class="lockup-mark"></span>
      <span class="lockup-name">QUORVEX</span>
    </div>

    <p class="address">
      <span class="legal-name">Quorvex Sweden AB</span><br>
      Bruksvägen 14, SE-175 43<br>
      JÄRFÄLLA, Sweden
    </p>

    <ul class="contacts">
      <li><svg viewBox="0 0 12 12"><path d="M3 0h6a1 1 0 0 1 1 1v10a1 1 0 0 1-1 1H3a1 1 0 0 1-1-1V1a1 1 0 0 1 1-1zm0 2v8h6V2z"/></svg>+46735 21 47 83</li>
      <li><svg viewBox="0 0 12 12"><path d="M2.5 1l2 2.2-1 1.3a7 7 0 0 0 4 4l1.3-1 2.2 2-1.2 1.5C5 10.5 1.5 7 1 2.2z"/></svg>+46 8 61 94 27</li>
      <li><svg viewBox="0 0 12 12"><path d="M0 2h12v8H0zm1 1v.3l5 3.4 5-3.4V3z"/></svg>info@quorvex-example.com</li>
    </ul>

    <div class="person">
      <p class="person-name">LENA HOLMQVIST</p>
      <p class="person-title">Chief Financial Officer (CFO)</p>
    </div>

    <p class="website">www.<b>quorvex-example</b>.com</p>
  </section>
</body>
</html>
```